Design logo, business cards, and web page for new web and bi development consulting company

I've started a Web and Business Intelligence development consulting company. We develop on Bramquist's stack, Visual Sudio and SQL Server. We develop responsive web sites and business intelligence platforms. I plan on focusing on small to medium sized business as my client base. I need a logo, business cards, and a one page web site. We will do more with the web site with you in the next six months if the business survives. The name of the company is Korvale Integration Solutions, Korvale for short.

Target Market(s)

small to medium sized businesses

Industry/Entity Type

Business

Contact Information for Business Card

logo
name
title
email
phone

Logo Text

Korvale Integration Solutions - web and data solutions

Coding

Coded - Design and coding required

Number of Pages Required

1 page

Font styles to use
Sans Serif

Colors
0355a3
0092cd
00a88f
6b449b

Requirements
Nice to have
• web and data solutions

```html
<!DOCTYPE html>
<html lang="en">
<head>
<meta charset="utf-8">
<title>Korvale Integration Solutions</title>
<link href="https://fonts.googleapis.com/css2?family=Open+Sans:wght@400;600&display=swap" rel="stylesheet">
<style>
  :root {
    --topbar: #5a2787;
    --brand: #6b2fa0;
    --hero-dark: #6a23a8;
    --hero-light: #a55bdc;
    --white: #ffffff;
    --ink: #444444;
    --line: #d9cfe6;
    --arrow-bg: rgba(40, 20, 60, 0.55);
  }
  * { margin: 0; padding: 0; box-sizing: border-box; }
  html, body {
    width: 1200px; height: 800px; overflow: hidden;
    background: var(--white);
    font-family: "Open Sans", Arial, sans-serif;
  }
  .page { width: 1200px; height: 800px; position: relative; overflow: hidden; }

  .topbar {
    height: 38px; background: var(--topbar); color: var(--white);
    display: flex; align-items: center; padding: 0 180px; font-size: 11px;
  }
  .topbar .contact-item { display: flex; align-items: center; gap: 8px; margin-right: 28px; }
  .topbar .social { margin-left: auto; display: flex; gap: 14px; }
  .topbar .social span { width: 10px; height: 10px; border-radius: 50%; background: var(--white); opacity: .85; }

  .header {
    height: 90px; display: flex; align-items: center; padding: 0 180px 0 186px;
    border-bottom: 1px solid #eee;
  }
  .brand { color: var(--brand); font-weight: 400; line-height: 1.1; }
  .brand .name { font-size: 38px; display: block; }
  .brand .tag { font-size: 17px; display: block; }
  .nav { margin-left: auto; display: flex; align-items: center; gap: 30px; font-size: 12px; color: var(--ink); }
  .nav a { color: inherit; text-decoration: none; position: relative; }
  .nav a.active { color: var(--brand); }
  .nav a.active::after {
    content: ""; position: absolute; left: -6px; right: -6px; top: 36px; height: 3px; background: var(--brand);
  }

  .hero {
    position: relative; height: 510px;
    background: linear-gradient(135deg, var(--hero-dark) 0%, var(--hero-light) 45%, var(--hero-dark) 100%);
  }
  .hero-art {
    position: absolute; left: 254px; top: 118px; width: 456px; height: 284px;
    border-radius: 10px; background: linear-gradient(180deg, #d8cce6 0%, #b9a4d3 100%); opacity: .9;
  }
  .hero-copy { position: absolute; left: 720px; top: 110px; }
  .hero-copy .line {
    display: block; width: max-content; margin-bottom: 12px; padding: 3px 10px;
    font-size: 24px; border: 2px solid var(--white); color: var(--white);
  }
  .hero-copy .line.filled { background: var(--white); color: var(--brand); }
  .hero-copy .gap { height: 22px; }
  .slide-arrow {
    position: absolute; top: 236px; width: 40px; height: 44px; background: var(--arrow-bg);
    display: flex; align-items: center; justify-content: center;
  }
  .slide-arrow.prev { left: 40px; }
  .slide-arrow.next { right: 50px; }
  .slide-dots { position: absolute; top: 420px; left: 640px; display: flex; gap: 6px; }
  .slide-dots span { width: 14px; height: 14px; border-radius: 50%; background: var(--white); }
  .slide-dots span.off { background: rgba(255,255,255,.45); }

  .features {
    height: 162px; display: flex; justify-content: center; gap: 20px; padding-top: 44px;
  }
  .feature {
    position: relative; width: 260px; height: 72px;
    display: flex; justify-content: center;
  }
  .feature::before {
    content: ""; position: absolute; left: 0; right: 0; top: 36px; height: 1px; background: var(--line);
  }
  .feature-icon {
    position: relative; width: 64px; height: 72px; border: 2px solid var(--line); border-radius: 6px;
    display: flex; align-items: center; justify-content: center; background: var(--white);
  }
</style>
</head>
<body>
<div class="page">
  <div class="topbar">
    <div class="contact-item">
      <svg width="10" height="16" viewBox="0 0 10 16"><rect x="1" y="1" width="8" height="14" rx="1.5" fill="none" stroke="#fff" stroke-width="1.4"/><circle cx="5" cy="12.5" r="0.9" fill="#fff"/></svg>
      Call Us Today! 1.555.555.5555
    </div>
    <div class="contact-item">
      <svg width="18" height="13" viewBox="0 0 18 13"><rect x="1" y="1" width="16" height="11" fill="none" stroke="#fff" stroke-width="1.4"/><path d="M1 1l8 6 8-6" fill="none" stroke="#fff" stroke-width="1.4"/></svg>
      info@yourdomain.com
    </div>
    <div class="social"><span></span><span></span><span></span><span></span><span></span></div>
  </div>

  <header class="header">
    <div class="brand"><span class="name">Korvale</span><span class="tag">Integration Solutions</span></div>
    <nav class="nav">
      <a class="active" href="#">Home</a><a href="#">Page</a><a href="#">Portfolio</a><a href="#">Blog</a>
      <a href="#">Shop</a><a href="#">Travel</a><a href="#">Shortcodes</a><a href="#">Features</a><a href="#">Contact</a>
      <svg width="22" height="22" viewBox="0 0 22 22"><circle cx="9" cy="9" r="7" fill="none" stroke="#6b2fa0" stroke-width="2.4"/><path d="M14 14l6 6" stroke="#6b2fa0" stroke-width="2.6" stroke-linecap="round"/></svg>
    </nav>
  </header>

  <section class="hero">
    <div class="hero-art" role="img" aria-label="Laptop illustration showing the website"></div>
    <div class="hero-copy">
      <span class="line filled">This Endless Options</span>
      <span class="line filled">Paired With Parallax Slider</span>
      <div class="gap"></div>
      <span class="line">Provides Endless Possibilites</span>
      <span class="line">All You Need Is Creativity</span>
    </div>
    <div class="slide-arrow prev"><svg width="10" height="14" viewBox="0 0 10 14"><path d="M8 1L2 7l6 6" fill="none" stroke="#fff" stroke-width="2"/></svg></div>
    <div class="slide-arrow next"><svg width="10" height="14" viewBox="0 0 10 14"><path d="M2 1l6 6-6 6" fill="none" stroke="#fff" stroke-width="2"/></svg></div>
    <div class="slide-dots"><span></span><span></span><span></span><span class="off"></span></div>
  </section>

  <section class="features">
    <div class="feature">
      <div class="feature-icon">
        <svg width="34" height="28" viewBox="0 0 34 28"><rect x="5" y="3" width="24" height="17" rx="1" fill="none" stroke="#6b2fa0" stroke-width="2"/><path d="M1 24h32" stroke="#6b2fa0" stroke-width="2.5"/></svg>
      </div>
    </div>
    <div class="feature">
      <div class="feature-icon">
        <svg width="30" height="30" viewBox="0 0 30 30"><rect x="1" y="1" width="28" height="28" rx="3" fill="#6b2fa0"/><path d="M9 13a6 6 0 0 1 11-3M21 17a6 6 0 0 1-11 3" fill="none" stroke="#fff" stroke-width="2"/><path d="M20 6v4h-4M10 24v-4h4" fill="none" stroke="#fff" stroke-width="2"/></svg>
      </div>
    </div>
    <div class="feature">
      <div class="feature-icon">
        <svg width="30" height="30" viewBox="0 0 30 30"><rect x="3" y="2" width="24" height="26" fill="none" stroke="#6b2fa0" stroke-width="2"/><path d="M3 10h24M3 17h24M3 24h24" stroke="#6b2fa0" stroke-width="1.5"/><circle cx="10" cy="10" r="2" fill="#6b2fa0"/><circle cx="18" cy="17" r="2" fill="#6b2fa0"/><circle cx="13" cy="24" r="2" fill="#6b2fa0"/></svg>
      </div>
    </div>
  </section>
</div>
</body>
</html>
```